1907 Zum Grillhof Website
Zielgruppe
Wir betreiben ein Hamburger-Restaurant. Alle Zutaten kommen wenn möglich, aus der Region. Wir benutzen keine Farb- und Konservierungsstoffe. Unser Fleisch ist ein frisches Bio-Rinderhack. Das Brot backen wir selber und die Saucen sind nach eigener Rezeptur hausgemacht. Der Käse wird in einem Familienbetrieb frisch für uns hergestellt. Jeder Gast kann sich seinen Burger frisch nach seinen Wünschen zusammenstellen und bei der Zubereitung zuschauen. Essen mit Herkunft aus Tradition!
Aufgabenstellung
Ansprechendes Design, welches unsere Philosophie und die Liebe zum Burger widerspiegelt. Frische Zutaten in wechselnden Slide-Shows, Wertschätzung der Rohprodukte und den Genuss beim Essen.

```html
<!DOCTYPE html>
<html lang="de">
<head>
<meta charset="utf-8">
<title>1907 Zum Grillhof</title>
<link rel="stylesheet" href="https://fonts.googleapis.com/css2?family=Source+Sans+3:wght@400;600;700&family=Gochi+Hand&display=swap">
<style>
:root{
  --orange:#c98130;
  --orange-bright:#e0963a;
  --leather-dark:#1e140e;
  --chalk:#141414;
  --chalk-light:#2a2a2a;
  --white:#f3ece2;
  --note:#9a9a9a;
  --muted:#7a5a3a;
  --footer:#1b130e;
}
*{margin:0;padding:0;box-sizing:border-box}
html,body{width:1200px;height:1014px;overflow:hidden;background:var(--footer)}
body{position:relative;font-family:"Source Sans 3",sans-serif}
.abs{position:absolute}

.topbar{left:0;top:0;width:1200px;height:24px;background:var(--leather-dark);border-bottom:1px solid #000}
.phone{left:306px;top:6px;font-size:8px;color:var(--orange)}
.social{width:14px;height:14px;border-radius:2px;background:var(--orange);opacity:.85}

.navband{left:0;top:24px;width:1200px;height:64px;background:linear-gradient(#4a3324,#3a281c 60%,#2b1d14);border-top:1px solid #5a4030;border-bottom:2px solid #120c08}
.navband::after{content:"";position:absolute;left:0;right:0;bottom:5px;border-bottom:1px dashed rgba(0,0,0,.45)}
.nav a{position:absolute;top:50px;font-size:11.5px;font-weight:700;color:var(--orange);text-decoration:none}
.nav a.active{top:44px;left:291px;width:58px;height:25px;line-height:25px;text-align:center;background:#1c120c;border-radius:13px;color:var(--orange-bright);box-shadow:inset 0 1px 3px #000}

.brand{left:552px;top:5px;width:96px;height:96px;border-radius:50%;background:var(--leather-dark);border:2px solid var(--white);display:flex;align-items:center;justify-content:center;text-align:center;z-index:3}
.brand span{font-size:15px;font-weight:700;color:var(--white);line-height:1.05}

.hero{left:0;top:88px;width:1200px;height:326px;background:radial-gradient(ellipse at 50% 45%,#8a7458 0%,#5e4c38 55%,#33271c 100%)}
.hero-title{left:0;top:200px;width:1200px;text-align:center;font-size:22px;font-weight:400;color:var(--white);text-shadow:0 1px 3px #000}
.hero-text{left:306px;top:229px;width:588px;text-align:center;font-size:11px;line-height:13.5px;color:var(--white);text-shadow:0 1px 2px #000}
.btn{top:273px;height:25px;width:138px;line-height:25px;text-align:center;font-size:9.5px;font-weight:600;color:#fff;border-radius:2px}
.btn-dark{left:454px;background:linear-gradient(#2a1c14,#120b07)}
.btn-orange{left:605px;background:linear-gradient(#e39b3e,#b86d22)}

.strip{left:0;top:414px;width:1200px;height:32px;background:linear-gradient(#2c1e15,#3b2819 50%,#24180f);border-top:2px solid #120c08}

.board{left:0;top:446px;width:1200px;height:380px;background:radial-gradient(ellipse at 50% 40%,var(--chalk-light),var(--chalk) 70%,#0a0a0a)}
.board-title{left:0;top:470px;width:1200px;text-align:center;font-family:"Gochi Hand",cursive;font-weight:400;font-size:29px;line-height:24px;color:var(--white)}
.burger{left:455px;top:588px;width:290px;height:210px;border-radius:48% 48% 40% 40%;background:radial-gradient(ellipse at 50% 40%,#d99a46,#a5502c 60%,#4a2a1a 100%)}
.label{font-family:"Gochi Hand",cursive;font-size:21px;color:var(--orange-bright)}
.note{font-family:"Gochi Hand",cursive;font-size:12.5px;line-height:13.5px;color:var(--note)}

.footband{left:0;top:826px;width:1200px;height:33px;background:linear-gradient(#3a281b,#2b1d13);border-top:2px solid #120c08}
.footer h4{position:absolute;top:890px;font-size:8px;font-weight:600;color:var(--orange)}
.footer .col{position:absolute;top:905px;font-size:7.7px;line-height:10.5px;color:var(--muted)}
.footer .col a{color:var(--muted);text-decoration:none;display:block}
.hours b{font-weight:600;color:var(--orange)}
.footmark{left:818px;top:882px;width:75px;height:75px;border-radius:50%;background:#2a1e15;opacity:.7}
</style>
</head>
<body>

<div class="abs topbar"></div>
<div class="abs phone">Telefon: +49 421 30190700</div>
<div class="abs social" style="left:866px;top:5px" aria-hidden="true"></div>
<div class="abs social" style="left:884px;top:5px" aria-hidden="true"></div>

<div class="abs navband"></div>
<nav class="nav">
  <a class="active" href="#">HOME</a>
  <a href="#" style="left:377px">ABOUT US</a>
  <a href="#" style="left:465px">OUR STORY</a>
  <a href="#" style="left:675px">OUR MENU</a>
  <a href="#" style="left:768px">EVENTS</a>
  <a href="#" style="left:843px">CONTACT</a>
</nav>
<div class="abs brand"><span>1907<br>Zum<br>Grillhof</span></div>

<section>
  <div class="abs hero" role="img" aria-label="Sepia photograph of the restaurant facade with doors, a bicycle and menu boards"></div>
  <h1 class="abs hero-title">Das Fast-Food-Urgestein findet seine Wurzeln</h1>
  <p class="abs hero-text">In 1885, two brothers sold in the U.S. state of New York in the city of Hamburg sandwiches with pork . But since pork was sold short , the men experimented with beef. This invention accordingly they called the birthplace of "hamburger" * .</p>
  <svg class="abs" style="left:274px;top:248px" width="14" height="26"><path d="M12 1 L2 13 L12 25" fill="none" stroke="#eee" stroke-width="1.2"/></svg>
  <svg class="abs" style="left:916px;top:248px" width="14" height="26"><path d="M2 1 L12 13 L2 25" fill="none" stroke="#eee" stroke-width="1.2"/></svg>
  <a class="abs btn btn-dark">MAKE RESERVATION</a>
  <a class="abs btn btn-orange">DOWNLOAD MENU</a>
</section>

<div class="abs strip"></div>

<section>
  <div class="abs board"></div>
  <h2 class="abs board-title">We at 1907 make the burger as it was<br>originally intended :</h2>
  <div class="abs burger" role="img" aria-label="Photograph of a burger with bun, beef patty, cheese, tomato, onion and lettuce"></div>

  <div class="abs label" style="left:301px;top:563px">Eigener Rezeptur Brot</div>
  <div class="abs note" style="left:303px;top:591px">It is a long established fact that<br>a reader will be distracted</div>
  <div class="abs label" style="left:735px;top:581px">Fleisch</div>
  <div class="abs note" style="left:737px;top:608px">ist 100% frisches<br>Bio-Rinderhack</div>
  <div class="abs label" style="left:306px;top:720px">Frische Zutaten</div>
  <div class="abs note" style="left:308px;top:748px">Lorem Ipsum is simply dummy<br>text of the printing and</div>
  <div class="abs label" style="left:743px;top:736px">Käse</div>
  <div class="abs note" style="left:745px;top:764px">wird in einem Familienbetrieb<br>frisch für uns hergestellt</div>

  <svg class="abs" style="left:0;top:0" width="1200" height="1014" fill="none" stroke="#d08a3a" stroke-width="1.2">
    <path d="M525 630 C490 632 470 625 463 615"/><path d="M460 622 L463 615 L470 619"/>
    <path d="M705 665 C735 660 752 650 755 640"/><path d="M750 645 L755 640 L757 647"/>
    <path d="M485 682 C450 688 425 700 420 718"/><path d="M416 712 L420 718 L425 712"/>
    <path d="M702 710 C705 730 718 748 736 750"/><path d="M730 745 L736 750 L730 754"/>
  </svg>
</section>

<div class="abs footband"></div>
<div class="abs social" style="left:867px;top:836px" aria-hidden="true"></div>
<div class="abs social" style="left:885px;top:836px" aria-hidden="true"></div>

<footer class="footer">
  <h4 style="left:309px">NAVIGATION</h4>
  <div class="col" style="left:309px">
    <a href="#">Home</a><a href="#">About us</a><a href="#">Out Story</a><a href="#">Our menu</a><a href="#">Events</a><a href="#">Contact</a>
  </div>
  <h4 style="left:427px">KONTAKT INFORMATION</h4>
  <div class="col" style="left:427px">
    1907 Zum Grillhof GmbH<br>Lindenweg 14<br>28203 Bremen<br>Geschäftsführerin: Petra Lindqvist<br>Telefon: +49 421 30190700<br>E-Mail:&nbsp; info@zumgrillhof.de
  </div>
  <h4 style="left:594px">FREUNDE DES GUTEN BURGER</h4>
  <div class="col hours" style="left:594px">
    Öffnungszeiten:<br>
    Montag - Donnerstag &nbsp;&nbsp;&nbsp;<b>11:30 Uhr bis 22:00 Uhr</b><br>
    Freitag - Samstag &nbsp;&nbsp;&nbsp;&nbsp;&nbsp;<b>11:30 Uhr bis 23:00 Uhr</b><br>
    Sonntag &nbsp;&nbsp;&nbsp;&nbsp;&nbsp;&nbsp;&nbsp;&nbsp;&nbsp;&nbsp;&nbsp;&nbsp;&nbsp;&nbsp;&nbsp;<b>16:00 Uhr bis 22:00 Uhr</b>
  </div>
  <div class="abs footmark"></div>
</footer>

</body>
</html>
```